Create a Graphic About YOURSELF and PixelHarbor

PixelHarbor would like you (designers) to create an awesome graphic to promote YOURSELF and your profile on PixelHarbor!

Your graphic should communicate your name, your services and should mention PixelHarbor.

The design should be perfect for sharing on Chatterly. Here's an example of what we'd like http://blog.pixelharbor-example.ca/article/333/pixelharbor-launches-3000-hire-me-social-design-contest

Once you submitted your design, we'd love you to share the design ('advertisement') and promote yourself and PixelHarbor to your friends and potential customers. So make your submissions great and get your friends to vote for your design by 'Liking' it on Chatterly!

Prizes:
$1500 - "PixelHarbor Community" prize awarded to the designer with the most Chatterly 'Likes'
5 x $50 for the next 5 'most liked' designs on Chatterly

$1000 - "Hire Me" prize awarded to the designer who receives the most client invites
5 x $50 for the next 5 'most invited' designers

In summary, this is a great opportunity for you to increase your exposure to PixelHarbor customers and win cash prizes. Show off your design skills and get hired by PixelHarbor customers from around the world!

Target Market(s)

Fans, friends and customers of YOU

Industry/Entity Type

Cash

Requirements
Must have
• 1) Include your PixelHarbor user name on the graphic so customers can find you in the PixelHarbor Designer Directory
2) Include the tagline "Hire Me on PixelHarbor.com!" in your graphic design.
3) Share your design's URL on our Chatterly wall at http://chatterly-example.com/pixelharbor and get your friends to 'like' your design.
Nice to have
• 1) Include a tagline that expresses your design approach/philosophy
2) Artwork dimensions: 403 x 403 px
3) You can submit more than 1 design!
Should not have
• You must own the copyright of any images you use including stock imagery.

```html
<!DOCTYPE html>
<html lang="en">
<head>
<meta charset="utf-8">
<title>Slatewell Logo House – Hire me on PixelHarbor.com</title>
<link href="https://fonts.googleapis.com/css2?family=Open+Sans:wght@400;700;800&display=swap" rel="stylesheet">
<style>
  :root {
    --board-dark: #1e1e1e;
    --board-mid: #3a3a3a;
    --board-light: #4a4a4a;
    --ink-white: #ffffff;
  }
  html, body {
    margin: 0;
    padding: 0;
    width: 1200px;
    height: 1200px;
    overflow: hidden;
    background: var(--board-dark);
  }
  .poster {
    position: relative;
    width: 1200px;
    height: 1200px;
    overflow: hidden;
    font-family: "Open Sans", Arial, sans-serif;
    color: var(--ink-white);
  }
  .poster__backdrop {
    position: absolute;
    inset: 0;
    background: radial-gradient(ellipse at 50% 40%, var(--board-light) 0%, var(--board-mid) 45%, var(--board-dark) 100%);
  }
  .brand-name {
    position: absolute;
    top: 235px;
    left: 0;
    width: 1200px;
    margin: 0;
    display: flex;
    flex-direction: column;
    align-items: center;
    font-weight: 800;
    color: var(--ink-white);
    text-transform: uppercase;
    line-height: 0.86;
  }
  .brand-name__top { font-size: 122px; letter-spacing: -3px; }
  .brand-name__middle { font-size: 240px; letter-spacing: -6px; }
  .brand-name__bottom { font-size: 236px; letter-spacing: -8px; }
  .hire-line {
    position: absolute;
    top: 770px;
    left: 0;
    width: 1200px;
    margin: 0;
    text-align: center;
    font-size: 52px;
    font-weight: 400;
  }
  .hire-site {
    position: absolute;
    top: 862px;
    left: 0;
    width: 1200px;
    margin: 0;
    text-align: center;
    font-size: 58px;
    font-weight: 700;
  }
</style>
</head>
<body>
  <main class="poster">
    <div class="poster__backdrop" role="img" aria-label="Dark grey wood-grain board background"></div>
    <h1 class="brand-name">
      <span class="brand-name__top">Slatewell</span>
      <span class="brand-name__middle">Logo</span>
      <span class="brand-name__bottom">House</span>
    </h1>
    <p class="hire-line">Hire me on</p>
    <p class="hire-site">PixelHarbor.com</p>
  </main>
</body>
</html>
```